Morning Harvest Psalm Journal for the Weary Traveler on the Narrow Road

This is not an Eastern meditation method. No images or themes from guru style or Eastern meditations from Hinduism or Buddhism will work. This is a Biblical Christian-based method. Some sort of Divine Light from Heaven may be the look. Some "ancient scroll" for the title to be written in may work.

```html
<!DOCTYPE html>
<html lang="en">
<head>
<meta charset="utf-8">
<title>Morning Harvest Psalm Journal – Book Cover</title>
<link rel="stylesheet" href="https://fonts.googleapis.com/css2?family=Cinzel:wght@400;500;600&family=Crimson+Text&display=swap">
<style>
  :root {
    --backdrop: #f1dcae;
    --sky-blue: #5f82b3;
    --sky-deep: #47699a;
    --sky-pale: #dfe3dc;
    --sky-cream: #efe3c4;
    --spine-band: rgba(96, 122, 150, 0.82);
    --spine-ink: #f4d3a0;
    --paper: #efe2c2;
    --paper-edge: #d9c39a;
    --ink: #33230f;
  }
  * { margin: 0; padding: 0; box-sizing: border-box; }
  html, body { width: 1200px; height: 1200px; overflow: hidden; }
  body { background: var(--backdrop); position: relative; }

  .book-jacket {
    position: absolute; left: 40px; top: 196px;
    width: 1120px; height: 808px;
    box-shadow: 0 6px 18px rgba(90, 60, 20, 0.35);
  }
  .panel { position: absolute; top: 0; height: 100%; overflow: hidden; }
  .back-cover { left: 0; width: 521px; }
  .spine { left: 521px; width: 78px; }
  .front-cover { left: 599px; width: 521px; }

  .sky-art { position: absolute; inset: 0; }
  .back-cover .sky-art {
    background:
      radial-gradient(ellipse 60% 35% at 55% 20%, var(--sky-pale), transparent 70%),
      radial-gradient(ellipse 70% 30% at 50% 62%, var(--sky-cream), transparent 75%),
      radial-gradient(ellipse 80% 25% at 40% 88%, var(--sky-deep), transparent 80%),
      linear-gradient(180deg, var(--sky-blue) 0%, #9fb4c6 35%, #c9d3cc 60%, #7f96b6 82%, #e6cfa2 100%);
  }
  .spine .sky-art {
    background: linear-gradient(180deg, #6f8fb5 0%, #b8c6c8 50%, #6c86a8 100%);
  }
  .spine .spine-band { position: absolute; inset: 0; background: var(--spine-band); }
  .front-cover .sky-art {
    background:
      radial-gradient(circle at 70% 74%, #ffffff 0%, #f7f2e2 9%, transparent 28%),
      radial-gradient(ellipse 70% 30% at 60% 85%, #cfd6d6, transparent 75%),
      radial-gradient(ellipse 60% 25% at 30% 80%, #7890b2, transparent 75%),
      linear-gradient(180deg, var(--sky-blue) 0%, #9db2c7 35%, #c3d0d2 60%, #b4c2c9 85%, var(--sky-deep) 100%);
  }

  .title-main, .title-sub, .subtitle-main, .subtitle-line, .author-name {
    font-family: "Cinzel", serif; color: var(--ink); position: absolute;
  }

  /* back cover */
  .back-title { position: absolute; left: 0; width: 100%; top: 96px; text-align: center; }
  .back-title .title-main { position: static; display: block; font-size: 62px; line-height: 62px; font-weight: 500; padding-left: 14px; }
  .back-title .title-sub { position: static; display: block; font-size: 31px; line-height: 34px; padding-left: 14px; }
  .blurb {
    position: absolute; left: 50px; width: 430px; top: 243px;
    font-family: "Crimson Text", serif; font-size: 13.6px; line-height: 17.4px;
    color: var(--ink); text-align: center;
  }
  .blurb p + p { margin-top: 17px; }

  /* spine */
  .spine-text {
    position: absolute; left: 50%; top: 30px;
    transform-origin: 0 0; transform: rotate(90deg) translateY(-50%);
    width: 748px; display: flex; justify-content: space-between;
    font-family: "Cinzel", serif; font-size: 27px; color: var(--spine-ink); white-space: nowrap;
  }

  /* front cover */
  .title-scroll {
    position: absolute; left: 78px; top: 49px; width: 361px; height: 239px;
    background: linear-gradient(180deg, var(--paper) 0%, #f3e8cc 50%, var(--paper-edge) 100%);
    border-radius: 6px;
  }
  .front-title { position: absolute; left: 78px; width: 361px; top: 122px; text-align: center; }
  .front-title .title-main { position: static; display: block; font-size: 50px; line-height: 56px; font-weight: 500; }
  .front-title .title-sub { position: static; display: block; font-size: 30px; line-height: 34px; }
  .subtitle-main { left: 72px; top: 328px; font-size: 27px; }
  .subtitle-line { left: 72px; top: 364px; font-size: 21px; }
  .author-name { left: 82px; top: 705px; font-size: 38px; font-weight: 500; letter-spacing: 1px; }
</style>
</head>
<body>
  <div class="book-jacket">
    <section class="panel back-cover">
      <div class="sky-art" role="img" aria-label="Painted heavenly sky with soft blue and golden clouds"></div>
      <h2 class="back-title">
        <span class="title-main">MORNING</span>
        <span class="title-sub">HARVEST PSALM JOURNAL</span>
      </h2>
      <div class="blurb">
        <p>Lorem ipsum dolor sit amet consectetur adipiscing elit felis, placerat phasellus nibh ornare aliquam eleifend nulla congue suspendisse, sodales massa rhoncus imperdiet sed sem scelerisque. Quis varius commodo euismod suspendisse vitae ornare at, luctus sed aliquam pretium erat venenatis donec, nec tempus platea sapien feugiat ante. In rhoncus venenatis quam quisque tortor consequat cubilia, praesent et dapibus velit magnis ad egestas vel, sociosqu pharetra sapien eros nulla nam.</p>
        <p>Elementum netus varius nibh etiam montes ullamcorper blandit, at nisi senectus suspendisse taciti eget ad, magna non massa conubia rutrum feugiat. Feugiat potenti iaculis lectus suspendisse eget enim sollicitudin, tristique dis per diam nec sed mattis taciti, hac in viverra cras nam non. Proin habitasse vulputate non augue morbi urna pellentesque auctor, facilisis ornare vestibulum sociis faucibus nisi hendrerit rutrum inceptos, nascetur quis mi vivamus class porta massa.</p>
      </div>
    </section>

    <section class="panel spine">
      <div class="sky-art" role="img" aria-label="Continuation of the cloudy sky behind the spine"></div>
      <div class="spine-band"></div>
      <div class="spine-text"><span>MORNING HARVEST</span><span>THOMAS ELLERY</span></div>
    </section>

    <section class="panel front-cover">
      <div class="sky-art" role="img" aria-label="Heavenly clouds with a burst of divine light shining through"></div>
      <div class="title-scroll" role="img" aria-label="Unrolled ancient parchment scroll on wooden rods"></div>
      <h1 class="front-title">
        <span class="title-main">MORNING</span>
        <span class="title-sub">HARVEST PSALM JOURNAL</span>
      </h1>
      <p class="subtitle-main">FOR THE WEARY TRAVELER</p>
      <p class="subtitle-line">ON THE NARROW ROAD</p>
      <p class="author-name">THOMAS ELLERY</p>
    </section>
  </div>
</body>
</html>
```